Book Cover for Content Marketing Design Process that Targets Creative Entreprenuers

Book Cover for Kindle and print. I like the design I have which I attached, but want the professional touch. The book takes readers through a 3-day creative process to design a written content management strategy for their product or service. It's very experiential, and uses a playful guiding metaphor throughout. Despite the playful non-linear approach, the result is a very comprehensive and practical content plan that puts value and authentic service to customers first.

The message the cover should convey is that it's possible for the business owner to attract the attention of customers, to generate excitement, and to connect with an audience on an emotional level. I estimate the book spine to be around 0.30" on a 6" x 9" cover. For Kindle, the imaged needs to be 2,560 x 1,600 JPG format, no more than 50MB.

Target Market(s)

Creative entrepreneurs, artists, artisans who sell online.

Industry/Entity Type

Consulting

Requirements
Must have
• This is a very creative, spiritual, energetic approach to content marketing. I would like the cover to set the stage for the experiential and creative process to come. Should appear bold and fun.
Nice to have
• What I like about the file attached: the expressive faces highlighting the idea of getting attention and attracting an audience, the playful font for "Playbook," the color scheme. I think the subtitle is important, but not sure if it should be on the cover or not.
Should not have
• Nothing that veers into child-like.

```html
<!DOCTYPE html>
<html lang="en">
<head>
<meta charset="UTF-8">
<title>Content Marketing Playbook – Book Cover</title>
<link rel="stylesheet" href="https://fonts.googleapis.com/css2?family=Roboto:wght@300;400;500&family=Roboto+Condensed:wght@300;700&display=swap">
<style>
  :root {
    --stage: #ffffff;
    --cover: #0c0b0b;
    --cover-edge: #050505;
    --rose: #e3c9bf;
    --rose-deep: #b99387;
    --blush-white: #f6ebe7;
    --label: #e9e2de;
    --glow: #6a5a52;
  }
  * { margin: 0; padding: 0; box-sizing: border-box; }
  html, body {
    width: 1200px; height: 800px; overflow: hidden;
    background: var(--stage);
  }
  .canvas {
    position: relative; width: 1200px; height: 800px;
  }
  .cover {
    position: absolute; left: 382px; top: 30px;
    width: 436px; height: 740px;
    background: var(--cover);
    box-shadow: inset 6px 0 0 var(--cover-edge);
    overflow: hidden;
    font-family: "Roboto", sans-serif;
    color: var(--rose);
    text-align: center;
  }
  .line { position: absolute; left: 0; width: 100%; line-height: 1; white-space: nowrap; }
  .kicker {
    font-family: "Roboto Condensed", sans-serif; font-weight: 300;
    font-size: 24px; letter-spacing: 0.5px;
  }
  .kicker-1 { top: 44px; }
  .kicker-2 { top: 72px; }
  .promise {
    font-family: "Roboto Condensed", sans-serif; font-weight: 700;
    font-size: 34px;
  }
  .promise small { font-size: 22px; font-weight: 700; }
  .promise-1 { top: 104px; }
  .promise-2 { top: 146px; }
  .artwork {
    position: absolute; left: 20px; top: 184px; width: 396px; height: 383px;
    background:
      radial-gradient(ellipse 42% 48% at 50% 45%, rgba(160,140,128,0.45), rgba(60,50,46,0.25) 55%, transparent 80%),
      linear-gradient(to bottom, transparent 70%, rgba(90,78,72,0.35) 92%, transparent);
  }
  .topic {
    font-weight: 400; font-size: 12px; letter-spacing: 3.6px; color: var(--label);
  }
  .topic-1 { top: 326px; }
  .topic-2 { top: 373px; font-size: 14px; letter-spacing: 5px; }
  .topic-3 { top: 420px; font-size: 11px; }
  .topic-4 { top: 465px; font-size: 11px; }
  .title { font-family: "Roboto", sans-serif; }
  .title-content {
    top: 503px; font-weight: 500; font-size: 70px; letter-spacing: -1px;
    color: var(--blush-white);
    font-family: "Roboto Condensed", sans-serif; font-weight: 700;
  }
  .title-marketing {
    top: 560px; font-weight: 300; font-size: 56px; color: var(--blush-white);
  }
  .title-playbook {
    top: 612px; font-weight: 300; font-size: 68px; color: var(--rose-deep);
    letter-spacing: 1px;
  }
  .tagline {
    top: 682px; font-family: "Roboto Condensed", sans-serif; font-weight: 300;
    font-size: 20px; color: var(--rose);
  }
</style>
</head>
<body>
<main class="canvas">
  <section class="cover">
    <div class="artwork" role="img" aria-label="Open book with swirling letters rising from its pages in a soft glow"></div>

    <p class="line kicker kicker-1">ATTRACT MORE ATTENTION</p>
    <p class="line kicker kicker-2">ONLINE WITH</p>
    <p class="line promise promise-1"><small>A</small> CONTENT STRATEGY</p>
    <p class="line promise promise-2"><small>THAT’S</small> FUN, MAGNETIC</p>

    <p class="line topic topic-1">PRODUCT DEVELOPMENT</p>
    <p class="line topic topic-2">MARKETING</p>
    <p class="line topic topic-3">ACCOUNTING</p>
    <p class="line topic topic-4">BRANDING</p>

    <h1>
      <span class="line title title-content">CONTENT</span>
      <span class="line title title-marketing">MARKETING</span>
      <span class="line title title-playbook">PLYBOOK</span>
    </h1>
    <p class="line tagline">AND STRAIGHT FROM THE HEART</p>
  </section>
</main>
</body>
</html>
```